use my brand and make an elegant business card  with it

Target Market(s)
male and female ' ages 25 to 45 age- who appreciate the highest quality goods, experiences, services, brands and relationships
Industry/Entity Type
Business
Requirements
Must have
- my logo integrated into the design-note the uploaded file
front: just logo and the phrase: New. Trend. Life. Style
back informations:
Mirela Dostan
Director
phone: +1 604 2917345
www.midostan.com
email: mireladostan@midostan.com
the pin of Facebook (F) and tweeter (T)
Nice to have
- contrast of the colors black gold and silver
Should not have
- cartoons or whimsical design

```html
<!DOCTYPE html>
<html lang="en">
<head>
<meta charset="utf-8">
<title>M.D. Dostan – Business Card</title>
<link rel="stylesheet" href="https://fonts.googleapis.com/css2?family=Josefin+Sans:wght@300;400&display=swap">
<style>
  :root {
    --backdrop: #2a2320;
    --card-black: #0e0e0f;
    --card-edge: #1c1c1e;
    --gold: #d8a562;
    --gold-soft: #b88a4e;
    --silver: #b9b9bd;
  }
  * { margin: 0; padding: 0; box-sizing: border-box; }
  html, body {
    width: 1200px;
    height: 1000px;
    overflow: hidden;
    background: var(--backdrop);
  }
  .canvas {
    width: 1200px;
    height: 1000px;
    display: flex;
    flex-direction: column;
    align-items: center;
    justify-content: center;
    gap: 70px;
  }
  .card {
    width: 560px;
    height: 320px;
    background: var(--card-black);
    border: 1px solid var(--card-edge);
    border-radius: 4px;
    box-shadow: 0 18px 40px rgba(0, 0, 0, 0.45);
    position: relative;
    color: var(--gold);
    font-family: "Josefin Sans", sans-serif;
  }
  .card-front {
    display: flex;
    flex-direction: column;
    align-items: center;
    justify-content: center;
  }
  .brand-emblem {
    width: 110px;
    height: 100px;
    border-radius: 6px;
    background: radial-gradient(circle, var(--gold-soft) 0%, #5a4024 70%, var(--card-black) 100%);
    opacity: 0.85;
    margin-bottom: 20px;
  }
  .brand-name {
    font-size: 40px;
    font-weight: 400;
    letter-spacing: 3px;
    line-height: 44px;
  }
  .brand-tagline {
    margin-top: 14px;
    font-size: 13px;
    font-weight: 300;
    letter-spacing: 3px;
    color: var(--silver);
    text-transform: uppercase;
  }
  .card-back .contact-block {
    position: absolute;
    right: 60px;
    top: 62px;
    width: 280px;
    text-align: center;
  }
  .contact-name {
    font-size: 20px;
    font-weight: 400;
    letter-spacing: 2px;
    line-height: 26px;
  }
  .contact-title {
    font-size: 12px;
    font-weight: 300;
    letter-spacing: 3px;
    text-transform: uppercase;
    color: var(--silver);
    margin: 4px 0 20px;
  }
  .contact-line {
    font-size: 14px;
    font-weight: 300;
    letter-spacing: 1.2px;
    line-height: 26px;
  }
  .social-row {
    display: flex;
    justify-content: center;
    gap: 12px;
    margin-top: 16px;
  }
  .social-dot {
    width: 16px;
    height: 16px;
    border-radius: 50%;
    background: var(--gold);
  }
</style>
</head>
<body>
  <main class="canvas">
    <section class="card card-front">
      <div class="brand-emblem" role="img" aria-label="Brand emblem: gold winged lion illustration"></div>
      <div class="brand-name">M.D. Dostan</div>
      <div class="brand-tagline">New. Trend. Life. Style</div>
    </section>
    <section class="card card-back">
      <div class="contact-block">
        <p class="contact-name">Mirela Dostan</p>
        <p class="contact-title">Director</p>
        <p class="contact-line">+1 604 2917345</p>
        <p class="contact-line">www.midostan.com</p>
        <p class="contact-line">mireladostan@midostan.com</p>
        <div class="social-row">
          <span class="social-dot" aria-label="Social profile"></span>
          <span class="social-dot" aria-label="Social profile"></span>
        </div>
      </div>
    </section>
  </main>
</body>
</html>
```